IT Consulting company Needs a Logo Design and Business Cards

I need a New Logo and Business Cards for an established IT Managed Services Company that specializes in flat-rate managed IT services. We provide Design and Build, Help Desk, Onsite and Remote Support Services.

Target Market(s)

Corporate Clients

Industry/Entity Type

It Company

Logo Text

Halbrook Computer Group

Requirements
Nice to have
• Tag Line= Technology at Lightning Speed

```html
<!DOCTYPE html>
<html lang="en">
<head>
<meta charset="utf-8">
<title>Halbrook Computer Group – Business Card</title>
<link href="https://fonts.googleapis.com/css2?family=Arimo:wght@400;700&display=swap" rel="stylesheet">
<style>
  :root {
    --bg: #2a2b2f;
    --card: #1e2124;
    --silver: #b9bcc0;
    --white: #f2f2f2;
    --blue: #2799d8;
    --ink: #15181b;
  }
  * { margin: 0; padding: 0; box-sizing: border-box; }
  html, body { width: 1200px; height: 800px; overflow: hidden; }
  body {
    background: var(--bg);
    font-family: "Arimo", Arial, sans-serif;
    position: relative;
  }
  .card {
    position: absolute;
    left: 320px;
    width: 560px;
    height: 320px;
    background: var(--card);
    box-shadow: 0 14px 30px rgba(0,0,0,0.45);
    overflow: hidden;
  }
  .card-front { top: 50px; }
  .card-back { top: 420px; }

  .front-brand {
    position: absolute;
    inset: 0;
    display: flex;
    align-items: center;
    justify-content: center;
    gap: 14px;
  }
  .brand-dot {
    width: 26px; height: 26px;
    border-radius: 50%;
    background: var(--silver);
  }
  .brand-name {
    font-weight: 700;
    font-size: 26px;
    letter-spacing: 2px;
    text-transform: uppercase;
    color: var(--silver);
    line-height: 1.1;
  }

  .back-brand {
    position: absolute;
    left: 34px;
    top: 92px;
    width: 240px;
  }
  .back-brand .brand-row { display: flex; align-items: center; gap: 10px; }
  .back-brand .brand-dot { width: 18px; height: 18px; background: var(--blue); }
  .back-brand .brand-name { font-size: 19px; color: var(--blue); letter-spacing: 1.5px; }
  .tagline {
    margin-top: 14px;
    font-size: 11px;
    letter-spacing: 1.2px;
    color: var(--silver);
  }

  .divider {
    position: absolute;
    left: 292px;
    top: 56px;
    width: 1px;
    height: 150px;
    background: var(--blue);
    opacity: 0.8;
  }

  .contact {
    position: absolute;
    left: 314px;
    top: 58px;
    color: var(--white);
  }
  .person-name { font-size: 21px; font-weight: 400; text-transform: uppercase; }
  .person-name .first { color: var(--blue); }
  .person-role { font-size: 11px; color: var(--white); margin-bottom: 14px; }
  .contact-line {
    display: flex; align-items: center; gap: 6px;
    font-size: 11.5px; line-height: 1.5;
  }
  .contact-line svg { width: 10px; height: 10px; flex: none; }
  .icon-spacer { width: 10px; flex: none; }

  .service-band {
    position: absolute;
    left: 0; right: 0;
    top: 246px;
    height: 32px;
    background: var(--blue);
    border-top: 2px solid var(--silver);
    border-bottom: 2px solid var(--silver);
    box-shadow: 0 -4px 0 var(--card), 0 -5px 0 var(--silver);
    display: flex; align-items: center; justify-content: center;
    font-size: 12px;
    letter-spacing: 1.6px;
    color: var(--ink);
  }
</style>
</head>
<body>
  <section class="card card-front">
    <div class="front-brand">
      <span class="brand-dot"></span>
      <span class="brand-name">Halbrook<br>Computer Group</span>
    </div>
  </section>

  <section class="card card-back">
    <div class="back-brand">
      <div class="brand-row">
        <span class="brand-dot"></span>
        <span class="brand-name">Halbrook<br>Computer Group</span>
      </div>
      <p class="tagline">Technology at Lightning Speed</p>
    </div>

    <div class="divider"></div>

    <div class="contact">
      <h1 class="person-name"><span class="first">Marcus</span> Reed</h1>
      <p class="person-role">Director</p>
      <p class="contact-line"><span class="icon-spacer"></span>PO BOX 418, Harbour Road</p>
      <p class="contact-line"><span class="icon-spacer"></span>2nd street Geelong</p>
      <p class="contact-line">
        <svg viewBox="0 0 10 10" aria-hidden="true"><path d="M2 0.5 L3.6 0.5 L4.2 2.8 L3 3.6 Q4 5.8 6.4 7 L7.2 5.8 L9.5 6.4 L9.5 8 Q9.5 9.5 8 9.5 Q1 9 0.5 2 Q0.5 0.5 2 0.5 Z" fill="#2799d8"/></svg>
        (555) 014 2290
      </p>
      <p class="contact-line">
        <svg viewBox="0 0 10 10" aria-hidden="true"><rect x="0.5" y="2" width="9" height="6.5" fill="#2799d8"/><path d="M0.5 2 L5 5.6 L9.5 2" fill="none" stroke="#1e2124" stroke-width="0.9"/></svg>
        info@halbrookgroup.com
      </p>
    </div>

    <div class="service-band">Build &amp; Design | Managed IT | Help Desk | Consulting</div>
  </section>
</body>
</html>
```